Bref créative
business card for an education project
QVN TA:-3182 (PHI) Learning Growth Sector Renewal Program
Simple
Tomas Belcastre, Ed.D
Team Leader and Education Specialist
5th Floor, Talong Bldg.,Bureau of Schooling (BurSC)
Sampit Avenue, Mandaluyong City
tbelcastre.consultant@qvn-example.org
I am a consultant on a project financed by the Coral Lending Union. The project will support the Government of the Philippines to implement its basic education reform program. Particularly by adding grades 11 and 12 to their secondary education program
The business card you develop for me will be a template used by other members of my team

```html
<!DOCTYPE html>
<html lang="en">
<head>
<meta charset="utf-8">
<title>LGSRP Business Card</title>
<link rel="stylesheet" href="https://fonts.googleapis.com/css2?family=Lato:wght@400;700;900&display=swap">
<style>
  :root {
    --stage: #e9ebee;
    --brand-blue: #2f67a6;
    --deep-blue: #234f86;
    --brand-red: #d8354a;
    --ink: #4a4f57;
    --rule: #d6d9de;
    --paper: #ffffff;
  }
  * { margin: 0; padding: 0; box-sizing: border-box; }
  html, body { width: 1200px; height: 864px; overflow: hidden; }
  body {
    background: var(--stage);
    font-family: "Lato", sans-serif;
    position: relative;
  }
  .card {
    position: absolute;
    width: 700px;
    height: 400px;
    border-radius: 26px;
    overflow: hidden;
    box-shadow: 0 6px 18px rgba(0,0,0,0.18);
  }
  .card-back { left: 90px; top: 20px; background: var(--brand-blue); }
  .card-front { left: 410px; top: 444px; background: var(--paper); }

  .brand { display: flex; flex-direction: column; align-items: center; position: absolute; }
  .brand-mark { display: flex; align-items: center; gap: 10px; }
  .brand-dot { width: 16px; height: 16px; border-radius: 50%; }
  .brand-name { font-weight: 900; font-size: 64px; letter-spacing: 1px; line-height: 1; }
  .brand-tagline { font-size: 10px; margin-top: 8px; width: 220px; text-align: center; line-height: 1.3; }

  .card-back .brand { left: 0; right: 0; top: 140px; }
  .card-back .brand-name { color: var(--paper); }
  .card-back .brand-dot { background: var(--paper); }
  .card-back .brand-tagline { color: var(--paper); }

  .card-front .brand { left: 40px; top: 150px; width: 250px; }
  .card-front .brand-name { color: var(--brand-blue); font-size: 58px; }
  .card-front .brand-dot { background: var(--brand-red); }
  .card-front .brand-tagline { color: var(--ink); }

  .divider { position: absolute; left: 320px; top: 70px; width: 1px; height: 220px; background: var(--rule); }

  .contact { position: absolute; left: 345px; top: 64px; width: 330px; }
  .contact-name { color: var(--brand-blue); font-weight: 700; font-size: 22px; }
  .contact-title { color: var(--ink); font-size: 13px; margin-top: 2px; margin-bottom: 18px; }
  .contact-list { list-style: none; }
  .contact-item { display: flex; align-items: flex-start; gap: 9px; color: var(--ink); font-size: 12px; line-height: 1.35; margin-bottom: 7px; }
  .contact-icon { flex: none; width: 16px; height: 16px; border-radius: 50%; background: var(--brand-blue); display: flex; align-items: center; justify-content: center; margin-top: 1px; }
  .contact-icon svg { width: 10px; height: 10px; }

  .waves { position: absolute; left: 0; bottom: 0; width: 700px; height: 140px; }
</style>
</head>
<body>
  <section class="card card-back" aria-label="Card back">
    <div class="brand">
      <div class="brand-mark">
        <span class="brand-name">LGSRP</span>
        <span class="brand-dot"></span>
      </div>
      <p class="brand-tagline">QVN TA:-3182 (PHI) Learning Growth Sector Renewal Program</p>
    </div>
  </section>

  <section class="card card-front" aria-label="Card front">
    <svg class="waves" viewBox="0 0 700 140" preserveAspectRatio="none" aria-hidden="true">
      <path d="M0 140 L0 120 C180 130 360 60 700 10 L700 30 C380 80 200 140 0 140 Z" fill="var(--brand-red)"/>
      <path d="M0 140 C220 140 420 90 700 40 L700 140 Z" fill="var(--brand-blue)"/>
    </svg>

    <div class="brand">
      <div class="brand-mark">
        <span class="brand-name">LGSRP</span>
        <span class="brand-dot"></span>
      </div>
      <p class="brand-tagline">QVN TA:-3182 (PHI) Learning Growth Sector Renewal Program</p>
    </div>

    <div class="divider"></div>

    <div class="contact">
      <h1 class="contact-name">Tomas Belcastre</h1>
      <p class="contact-title">Team Leader and Education Specialist</p>
      <ul class="contact-list">
        <li class="contact-item">
          <span class="contact-icon"><svg viewBox="0 0 10 10"><path d="M5 0.5a3 3 0 0 1 3 3c0 2.2-3 6-3 6s-3-3.8-3-6a3 3 0 0 1 3-3z" fill="#fff"/><circle cx="5" cy="3.5" r="1.1" fill="var(--brand-blue)"/></svg></span>
          <span>5th Floor, Talong Bldg.,Bureau of Schooling (BurSC)<br>Sampit Avenue, Verdano City</span>
        </li>
        <li class="contact-item">
          <span class="contact-icon"><svg viewBox="0 0 10 10"><path d="M2.5 1l1.5 2-1 1c.6 1.3 1.6 2.3 2.9 2.9l1-1 2 1.5-1 1.6C4.5 9 1 5.5 1 2z" fill="#fff"/></svg></span>
          <span>(48) 721-0394</span>
        </li>
        <li class="contact-item">
          <span class="contact-icon"><svg viewBox="0 0 10 10"><rect x="3" y="0.5" width="4" height="9" rx="0.8" fill="#fff"/><rect x="3.8" y="1.5" width="2.4" height="5.5" fill="var(--brand-blue)"/></svg></span>
          <span>0861-230-5577</span>
        </li>
        <li class="contact-item">
          <span class="contact-icon"><svg viewBox="0 0 10 10"><rect x="1" y="2.5" width="8" height="5.5" fill="#fff"/><path d="M1 2.5l4 3 4-3" stroke="var(--brand-blue)" stroke-width="0.8" fill="none"/></svg></span>
          <span>tbelcastre.consultant@qvn-example.org</span>
        </li>
        <li class="contact-item">
          <span class="contact-icon"><svg viewBox="0 0 10 10"><circle cx="5" cy="5" r="3.8" fill="none" stroke="#fff" stroke-width="0.9"/><ellipse cx="5" cy="5" rx="1.6" ry="3.8" fill="none" stroke="#fff" stroke-width="0.8"/><path d="M1.2 5h7.6" stroke="#fff" stroke-width="0.8"/></svg></span>
          <span>www.lgsrp-example.org</span>
        </li>
      </ul>
    </div>
  </section>
</body>
</html>
```